Luxury Inclusive Beauty Brand Needs Labels & Boxes for Product Line

We need updated labels and boxes for our cosmetic and skin care line. Our company is BRISA + KO. and we focus on providing upscale, natural and organic beauty products inclusive of diverse and deeper skin tones for women of color, especially black women. We have a seven piece skin care collection called DERMAVA Tamarind Collection and a mineral make-up line consisting of eight products. The design of all products should be the same with just dimensions and title/ingredient list differences. We would like to see designs that use our coral color e85350, work well on black packaging (bottles, lipstick tubes etc.) and include white and other additional pretty colors, metallics or patterns representative of ethnic (AFRICAN), bohemian or tribal influence. The final design should communicate luxury, floral/fauna environmentalism, and afrocentric culture influences.
We have included files of various prints we like and the type of lifestyle our customer aspires to/is attracted to. We have included in the files below some examples of packaging we like but we want something original to capture the attention of our target market, upper income health and ethnic conscious black women age 30 - 55 who love natural and organic products. The names of our products include the list below however if design can be submitted showing design on 1 tall box and 1 short box and 1 lipstick size box that would be great:
DERMAVA Tamarind Collection Cleansing Oil (dropper)
DERMAVA Tamarind Collection Balancing Toner (tall spray bottle)
DERMAVA Tamarind Collection Moisturizing Serum (dropper)
DERMAVA Tamarind Collection Moisturizing Cream (short box jar)
DERMAVA Tamarind Lip Scrub (short box - jar)
Luminous Mineral Foundation (short box- jar)
CC Cream
Moisturizing Lip Stick (lipstick box)
WINKORA Natural Mascara
Pimsy Tamsy Lip Crayon
Gel Eye Liner
Organic Make-up Remover (tall spray bottle)
Face & Eye Primer
Final dimensions /dies of boxes can be sent to winner of design competition.
women of color, age 30-55, income 50 - 150K, natural hair and organic lifestyle, yoga
Cosmetics
- label and box
- include the color e85350
- include logo
- easy way to differentiate skincare from make-up products

```html
<!DOCTYPE html>
<html lang="en">
<head>
<meta charset="utf-8">
<title>BRISA + KO. Packaging Labels</title>
<link rel="stylesheet" href="https://fonts.googleapis.com/css2?family=Josefin+Sans:wght@400;600&family=Great+Vibes&display=swap">
<style>
  :root {
    --bg: #e2e2e2;
    --black: #111111;
    --black-soft: #1c1c1c;
    --gold: #b38b4d;
    --gold-light: #c9a46a;
    --coral: #e85350;
    --teal: #2a9a86;
    --brown-dark: #5a3526;
    --brown-light: #c7a89b;
  }
  * { margin: 0; padding: 0; box-sizing: border-box; }
  html, body { width: 1200px; height: 899px; overflow: hidden; background: var(--bg); }
  body { position: relative; font-family: "Josefin Sans", sans-serif; }

  .pattern-band {
    position: absolute;
    background: linear-gradient(90deg, var(--coral), var(--teal) 50%, var(--coral));
  }

  /* Jar label */
  .jar-label {
    position: absolute; left: 128px; top: 478px; width: 310px; height: 187px;
    background: linear-gradient(90deg, var(--brown-dark), #8a5f4e 55%, var(--brown-light));
    border-radius: 0 0 10px 10px;
  }
  .jar-label .pattern-band { left: 0; top: 0; width: 100%; height: 30px; }
  .jar-label .product-name {
    position: absolute; left: 0; right: 0; top: 104px; text-align: center;
    font-size: 31px; font-weight: 600; letter-spacing: 1px; color: var(--gold-light);
  }
  .jar-label .product-type {
    position: absolute; left: 0; right: 0; top: 149px; text-align: center;
    font-size: 8px; letter-spacing: 2px; color: var(--gold);
  }

  /* Dropper label */
  .dropper-label {
    position: absolute; left: 522px; top: 436px; width: 155px; height: 209px;
    background: var(--black);
  }
  .brand-mark {
    position: absolute; left: 0; right: 0; text-align: center;
    font-size: 6px; letter-spacing: 0.5px; color: var(--gold);
  }
  .brand-mark .dot {
    display: block; width: 18px; height: 18px; margin: 0 auto 5px;
    border: 1px solid var(--gold); border-radius: 50%;
  }
  .dropper-label .brand-mark { top: 18px; }
  .dropper-label .product-name {
    position: absolute; left: 0; right: 0; top: 74px; text-align: center;
    font-size: 28px; font-weight: 600; letter-spacing: 0.5px; color: var(--gold-light);
  }
  .dropper-label .collection {
    position: absolute; left: 0; right: 0; top: 102px; text-align: center;
    font-family: "Great Vibes", cursive; font-size: 15px; color: var(--gold);
  }
  .dropper-label .product-type {
    position: absolute; left: 0; right: 0; top: 145px; text-align: center;
    font-size: 7px; letter-spacing: 1.5px; color: var(--gold);
  }
  .dropper-label .pattern-band { left: 0; top: 168px; width: 100%; height: 28px; }

  /* Tube label */
  .tube-label {
    position: absolute; left: 766px; top: 177px; width: 217px; height: 532px;
    background: var(--black-soft);
  }
  .tube-label .brand-mark { top: 32px; font-size: 7px; }
  .tube-label .brand-mark .dot { width: 30px; height: 30px; margin-bottom: 10px; }
  .tube-label .vertical-text {
    position: absolute; left: 0; top: 0;
    transform-origin: 0 0; transform: rotate(-90deg);
    white-space: nowrap;
  }
  .tube-label .product-name {
    left: 33px; top: 388px; font-size: 42px; font-weight: 600; letter-spacing: 1px; color: var(--gold);
  }
  .tube-label .product-type {
    left: 78px; top: 388px; font-size: 15px; letter-spacing: 4px; color: var(--gold);
  }
  .tube-label .pattern-band { left: 20px; top: 408px; width: 180px; height: 44px; }
  .tube-label .cap-band {
    position: absolute; left: 20px; top: 452px; width: 180px; height: 80px;
    background: #202020; border-top: 1px solid #2c2c2c;
  }
</style>
</head>
<body>
  <section class="jar-label">
    <div class="pattern-band" role="img" aria-label="Coral, teal and black geometric floral pattern band"></div>
    <h2 class="product-name">TONIVA</h2>
    <p class="product-type">[PRESSED POWDER]</p>
  </section>

  <section class="dropper-label">
    <div class="brand-mark"><span class="dot"></span>BRISA + KO.</div>
    <h2 class="product-name">DERMAVA</h2>
    <p class="collection">Tamarind Collection</p>
    <p class="product-type">[CLEANSING OIL]</p>
    <div class="pattern-band" role="img" aria-label="Coral and teal floral pattern border"></div>
  </section>

  <section class="tube-label">
    <div class="brand-mark"><span class="dot"></span>BRISA + KO.</div>
    <h2 class="vertical-text product-name">TONIVA</h2>
    <p class="vertical-text product-type">[BB CREAM]</p>
    <div class="pattern-band" role="img" aria-label="Coral and teal floral pattern border"></div>
    <div class="cap-band"></div>
  </section>
</body>
</html>
```